Business Card Design

Need a new business card to represent our legal vertical focus. attached is an example of our old business card and newest logo. we would like the card to also identify "Legal Tech" as a tag line of business.

Our new address is
7381 Harrowgate Linden Rd.
Suite 418
Cincinnati, OH 45917

we no longer have a fax number.

Target Market(s)

Tech Consulting for Law Firms

Industry/Entity Type

Legal

Contact Information for Business Card

should use logo and colors. we are a b2b company

Other font styles liked:
• tahoma

Requirements
Must have
• all print should be in lower case just as shown in photos. tag line should not
Should not have
• pinstripes or drop shadows

```html
<!DOCTYPE html>
<html lang="en">
<head>
<meta charset="utf-8">
<title>LinkVane Legal Tech – Business Card</title>
<link rel="stylesheet" href="https://fonts.googleapis.com/css2?family=Arimo:wght@400;700&display=swap">
<style>
  :root {
    --navy: #253c80;
    --navy-text: #24357a;
    --orange: #ec4f26;
    --paper: #f3f3f3;
    --white: #ffffff;
    --stage: #2b2b2b;
  }
  * { box-sizing: border-box; margin: 0; padding: 0; }
  html, body { width: 1200px; height: 800px; overflow: hidden; }
  body {
    background: var(--stage);
    font-family: "Arimo", Arial, sans-serif;
    position: relative;
  }
  .card {
    position: absolute;
    top: 251px;
    width: 525px;
    height: 299px;
    overflow: hidden;
  }
  .card--front { left: 68px; background: var(--navy); }
  .card--back { left: 608px; background: var(--paper); }

  /* front */
  .front-brand {
    position: absolute;
    right: 44px;
    top: 52px;
    text-align: right;
    color: var(--white);
  }
  .front-brand .brand-name {
    display: block;
    font-size: 60px;
    font-weight: 700;
    line-height: 1;
    letter-spacing: -1px;
  }
  .front-brand .tagline {
    display: block;
    font-size: 13px;
    font-weight: 700;
    margin-top: 1px;
  }
  .services {
    position: absolute;
    top: 166px;
    list-style: none;
    color: #e6e9f2;
    font-size: 12.5px;
    line-height: 15.6px;
  }
  .services--left { left: 188px; }
  .services--right { left: 384px; }
  .services li::before { content: "> "; color: var(--orange); }
  .front-url {
    position: absolute;
    left: 44px;
    right: 40px;
    top: 266px;
    display: flex;
    justify-content: space-between;
    color: var(--orange);
    font-size: 13px;
    font-weight: 700;
  }

  /* back */
  .swoosh { position: absolute; left: 0; top: 0; }
  .back-brand {
    position: absolute;
    left: 72px;
    top: 100px;
    color: var(--navy-text);
    text-align: right;
  }
  .back-brand .brand-name {
    display: block;
    font-size: 36px;
    font-weight: 700;
    line-height: 1;
    letter-spacing: -0.5px;
  }
  .back-brand .tagline {
    display: block;
    font-size: 9px;
    font-weight: 700;
    margin-top: 1px;
  }
  .contact {
    position: absolute;
    left: 299px;
    top: 44px;
    color: var(--navy-text);
  }
  .contact .person-name {
    color: var(--orange);
    font-size: 22px;
    font-weight: 700;
    line-height: 1;
  }
  .contact .person-title { font-size: 12.5px; margin-top: 1px; }
  .contact address {
    font-style: normal;
    font-size: 14px;
    line-height: 15.5px;
    margin-top: 18px;
  }
  .contact-lines { list-style: none; margin-top: 20px; font-size: 14px; line-height: 17px; }
  .contact-lines li { display: flex; align-items: center; gap: 4px; }
  .contact-lines .arrow { color: var(--orange); }
  .contact-lines .web { font-weight: 700; }
  .contact-lines svg { width: 12px; height: 12px; flex: none; }
</style>
</head>
<body>

<section class="card card--front" aria-label="Card front">
  <div class="front-brand">
    <span class="brand-name">LinkVane</span>
    <span class="tagline">Legal Tech</span>
  </div>
  <ul class="services services--left">
    <li>managed services</li>
    <li>backup/disaster recovery</li>
    <li>it consulting</li>
    <li>virtualization</li>
    <li>email / spam protection</li>
  </ul>
  <ul class="services services--right">
    <li>hosted solutions</li>
    <li>cloud services</li>
    <li>helpdesk</li>
    <li>mobility</li>
    <li>legal technology</li>
  </ul>
  <div class="front-url" aria-label="www.linkvane.net">
    <span>w</span><span>w</span><span>w</span><span>.</span><span>l</span><span>i</span><span>n</span><span>k</span><span>v</span><span>a</span><span>n</span><span>e</span><span>.</span><span>n</span><span>e</span><span>t</span>
  </div>
</section>

<section class="card card--back" aria-label="Card back">
  <svg class="swoosh" width="525" height="299" viewBox="0 0 525 299" aria-hidden="true">
    <path d="M0 226 C120 250 240 266 330 264 C420 262 480 246 525 233 L525 299 L0 299 Z" fill="var(--navy)"/>
    <path d="M0 198 C90 230 220 256 400 262 C260 262 110 244 0 222 Z" fill="var(--orange)"/>
  </svg>

  <div class="back-brand">
    <span class="brand-name">LinkVane</span>
    <span class="tagline">Legal Tech</span>
  </div>

  <div class="contact">
    <h1 class="person-name">daniel p. merrow, jr.</h1>
    <p class="person-title">president &amp; virtual cio</p>
    <address>
      7381 Harrowgate Linden Rd.<br>
      Suite 418<br>
      Cincinnati, OH 45917
    </address>
    <ul class="contact-lines">
      <li>
        <svg viewBox="0 0 12 12" aria-label="phone"><rect x="1" y="1" width="10" height="10" rx="1.5" fill="var(--orange)"/><rect x="3" y="3" width="2" height="6" fill="var(--paper)"/><rect x="6" y="3" width="3" height="2" fill="var(--paper)"/></svg>
        <span class="arrow">&gt;</span> 513.481.0736
      </li>
      <li>
        <svg viewBox="0 0 12 12" aria-label="email"><rect x="0.5" y="2" width="11" height="8" fill="var(--orange)"/><path d="M0.5 2 L6 6.5 L11.5 2" fill="none" stroke="var(--paper)" stroke-width="1"/></svg>
        <span class="arrow">&gt;</span> dmerrow@linkvane.net
      </li>
      <li>
        <svg viewBox="0 0 12 12" aria-label="web"><circle cx="6" cy="6" r="5.2" fill="none" stroke="var(--orange)" stroke-width="1.3"/><ellipse cx="6" cy="6" rx="2.2" ry="5.2" fill="none" stroke="var(--orange)" stroke-width="1"/><path d="M1 6 H11" stroke="var(--orange)" stroke-width="1"/></svg>
        <span class="arrow">&gt;</span> <span class="web">www.linkvane.net</span>
      </li>
    </ul>
  </div>
</section>

</body>
</html>
```